Looking for Landingpage / Website Designer

We are looking for a Web Designer / Developer for our upcoming Start Up Websites. The first project will be a simple responsive business website with a CTA- Button and an optional Newsletter Opt-In. We do aim for a modern online business approach, since we are a young company.

It is necessary to understand, that we need a conversion orientated design, not a wordpress blog with widgets and galleries.

We are currently discussing how it is going to happen and what preferences we need to focus on.

What we know is, that it should be more of a landing page with an option of adding 2 or 3 Navigation points.

We even thought about using services like plumvesta.com or crintofold.com to have an easier approach for future customizations and A/B testing.

We'd love to see how you fit the design/colors to the upcoming logo
(which is not the final version yet )

hope you can do something about that.

For the Structure.

1. Bracket

Slogan plus a preview text of what we are offering. On the right side a video placeholder plus CTA button.

2. Bracket

Illustrating 3 Benefits. On the right side - Opt in for Contact/Newsletter and CTA Button

3. Bracket

Picture with text just like you have it with the testimonial

You can orientate yourself towards to that landing page example as well:

http://cdn2.zorvellink.net/hub/53/file-581676469-png/Blog-Related_Images/plumvesta_landing_page.png?t=1416543075530

If our collaboration is going well, we would like to stay in touch for further projects.
Updates

Reason: There are 3 Design we do really like but, don't fit exactly our needs. 5 Days max.

Reason: For final adjustments.

I just uploaded the final logo :) Thank you for your commitment so far!

Target Market(s)

Our targeted audience could be almost everybody, who looks for an average paid side job (students, unemployed, house wives and whatever you can imagine). Maybe this is enough information for you to get a mere perception of what this is all about.

Industry/Entity Type

Business

Coding

Coded - Design and coding required

Font styles to use
Serif
Sans Serif

Colors
acd037
5c5c5c
33a6d7

Requirements
Must have
• Registration Opt-In
Responsive on any Device
Customizable
A benefits navigation just like in that example I've uploaded.
Nice to have
• As fast as possible ;D

```html
<!DOCTYPE html>
<html lang="en">
<head>
<meta charset="utf-8">
<title>iCompany – Advertising Service</title>
<link rel="stylesheet" href="https://fonts.googleapis.com/css2?family=Open+Sans:ital,wght@0,300;0,400;0,600;0,700;0,800;1,700;1,800&display=swap">
<style>
:root{
  --green:#acd037;
  --green-deep:#8aa52c;
  --grey:#5c5c5c;
  --blue:#33a6d7;
  --blue-deep:#2a8fbb;
  --white:#ffffff;
  --ink:#1e1e1e;
  --field:#ffffdc;
  --icon:#bdbdbd;
}
*{margin:0;padding:0;box-sizing:border-box}
html,body{width:834px;height:1200px;overflow:hidden;background:var(--white)}
body{font-family:"Open Sans",Arial,sans-serif;position:relative}
.abs{position:absolute}

/* header */
.site-header{left:0;top:0;width:834px;height:58px;background:var(--grey)}
.brand{left:82px;top:13px;display:flex;align-items:center;gap:10px;color:var(--white);font-weight:700;font-size:22px;white-space:nowrap}
.brand-mark{width:26px;height:26px;background:var(--blue)}
.proud{left:360px;top:21px;color:var(--blue);font-size:11px;white-space:nowrap}
.partners{left:556px;top:20px;display:flex;gap:22px;color:var(--white);font-size:11px;font-weight:600;white-space:nowrap}

/* hero */
.hero{left:0;top:58px;width:834px;height:398px;background:var(--green)}
.headline{left:84px;top:100px;color:var(--white);font-weight:300;line-height:1;white-space:nowrap}
.headline .l1{font-size:43px;display:block;letter-spacing:.5px}
.headline .l2{display:inline-block;margin-top:8px;background:var(--grey);font-size:47px;padding:2px 6px 4px}
.headline .l3{display:block;font-size:36px;margin-top:8px;letter-spacing:.5px}
.intro{left:86px;top:272px;width:370px;font-size:13.4px;line-height:18.5px;color:var(--ink)}
.intro em{color:var(--white);font-weight:800}

.newsletter-shadow{left:513px;top:127px;width:279px;height:269px;background:var(--green-deep);opacity:.55}
.newsletter{left:497px;top:110px;width:277px;height:268px;background:var(--white);border:3px solid var(--grey)}
.newsletter h2{position:absolute;left:66px;top:26px;font-size:16.5px;font-weight:800;color:var(--ink);white-space:nowrap}
.newsletter p{position:absolute;left:66px;top:48px;font-size:12px;font-weight:600;color:var(--ink);white-space:nowrap}
.field{position:absolute;left:33px;width:203px;height:38px;background:var(--field);border:2px solid #cfcfcf;border-radius:6px}
.submit{position:absolute;left:36px;top:206px;width:197px;height:33px;background:var(--grey);color:var(--green);font-weight:800;font-size:19px;text-align:center;line-height:33px;letter-spacing:.5px}

/* benefit tabs */
.blue-band{left:0;top:456px;width:834px;height:302px;background:var(--blue)}
.tab{top:432px;height:44px;background:var(--grey);color:var(--white);font-size:22px;font-weight:300;display:flex;align-items:center;gap:14px;padding-left:18px;box-shadow:0 3px 4px rgba(0,0,0,.25);white-space:nowrap}
.tab svg{flex:none}

/* featured */
.feature-shadow{left:94px;top:531px;width:252px;height:165px;background:var(--blue-deep)}
.feature-photo{left:78px;top:515px;width:252px;height:165px;border:4px solid var(--grey);background:linear-gradient(135deg,#9a9a9a,#5e5e5e 60%,#3f3f3f)}
.feature h3{position:absolute;left:376px;top:512px;font-size:17px;font-weight:800;color:var(--ink);white-space:nowrap}
.feature-text{left:376px;top:541px;width:400px;font-size:12.5px;line-height:18px;color:var(--white);font-weight:600}
.feature-text p+p{margin-top:18px}
.feature-more{left:600px;top:670px;width:162px;text-align:right;color:var(--white);font-style:italic;font-weight:800;font-size:12.5px}

/* call to action */
.cta-band{left:0;top:768px;width:834px;height:110px;background:var(--grey)}
.cta-text{left:74px;top:796px;color:var(--green);font-weight:800;font-size:19.5px;line-height:22px;white-space:nowrap}
.cta-button{left:584px;top:796px;width:195px;height:50px;background:var(--blue);display:flex;align-items:center;gap:14px;padding-left:4px;color:var(--white);font-weight:700;font-size:20px;white-space:nowrap}
.cta-button svg{flex:none}

/* testimonials */
.voices-art{left:60px;top:910px;width:260px;height:200px;background:radial-gradient(ellipse at 45% 55%,#d6d6d6,#eeeeee 70%,#ffffff);border-radius:8px}
.voices-title{left:92px;top:966px;width:320px;text-align:center;color:var(--blue);font-weight:800;font-size:27px;line-height:33px;white-space:nowrap}
.quote{left:430px;width:344px;height:74px}
.avatar{position:absolute;left:0;top:0;width:70px;height:70px;border-radius:50%;border:3px solid #e3e3e3;background:linear-gradient(160deg,#e8cfae,#b49a7f)}
.quote p{position:absolute;left:93px;top:12px;width:252px;font-size:9px;line-height:11.4px;font-weight:700;color:var(--ink)}
.quote cite{position:absolute;right:0;top:57px;font-size:9px;font-weight:800;font-style:italic;color:var(--blue);white-space:nowrap}

.site-footer{left:0;top:1178px;width:834px;height:22px;background:var(--grey);color:#dcdcdc;font-size:8.5px;text-align:center;line-height:22px}
</style>
</head>
<body>

<header class="abs site-header"></header>
<div class="abs brand"><span class="brand-mark"></span>Company Name</div>
<div class="abs proud">We are Proud to advertise for.....</div>
<div class="abs partners"><span>Harlowe</span><span>Vessa</span><span>Quillsoft</span><span>Brantmoor</span></div>

<section class="abs hero"></section>
<h1 class="abs headline">
  <span class="l1">ICOMPANY&nbsp; IS THE</span>
  <span class="l2">MOST EFFECTIVE</span>
  <span class="l3">ADVERTISING SERVICE</span>
</h1>
<p class="abs intro">Rebounder is the simplest and most effective self-serve display retargeting platform. Your ads will stay in front of your qualified audience to make your brand and increase your conversions. <em>GET STARTED!</em></p>

<div class="abs newsletter-shadow"></div>
<form class="abs newsletter">
  <h2>GET FREE NEWSLETTER</h2>
  <p>at your inbox for Latest Offers!!!</p>
  <div class="field" style="top:101px"></div>
  <div class="field" style="top:150px"></div>
  <div class="submit">SUBMIT</div>
</form>

<div class="abs blue-band"></div>

<nav>
  <div class="abs tab" style="left:80px;width:212px">
    <svg width="28" height="18" viewBox="0 0 28 18" aria-hidden="true"><circle cx="8" cy="5" r="4" fill="#bdbdbd"/><rect x="2" y="10" width="12" height="8" rx="2" fill="#bdbdbd"/><circle cx="20" cy="5" r="4" fill="#bdbdbd"/><rect x="14" y="10" width="12" height="8" rx="2" fill="#bdbdbd"/></svg>WHO WE ARE</div>
  <div class="abs tab" style="left:319px;width:213px;gap:26px">
    <svg width="20" height="22" viewBox="0 0 20 22" aria-hidden="true"><path d="M2 10h4v11H2zM7 10l4-8c2 0 3 1 3 3l-1 4h5c1 0 2 1 2 2l-2 8c0 1-1 2-2 2H7z" fill="#bdbdbd"/></svg>WHY US</div>
  <div class="abs tab" style="left:558px;width:212px">
    <svg width="20" height="24" viewBox="0 0 20 24" aria-hidden="true"><path d="M6 2c1-1 3 0 3 1v8l7 2c2 1 2 2 2 3l-2 8H7L2 15c0-1 1-2 2-1l2 2z" fill="#bdbdbd"/></svg>GET STARTED</div>
</nav>

<section class="feature">
  <div class="abs feature-shadow"></div>
  <div class="abs feature-photo" role="img" aria-label="Black and white photo of two businesspeople shaking hands"></div>
  <h3>THIS IS FEATURED HEADING</h3>
  <div class="abs feature-text">
    <p>This is dummy text and real content will be here very soon.&nbsp; This is dummy text for now and actual content will be here very soon. This is dummy text and real content will be here very soon.&nbsp; This is dummy text for now and actual content will be here very soon.</p>
    <p>This is dummy text and real content will be here very soon.&nbsp; This is dummy text for now and actual content will ...</p>
  </div>
  <div class="abs feature-more">GET STARTED!</div>
</section>

<section class="abs cta-band"></section>
<p class="abs cta-text">LOOKING FORWARD TO AN EFFECTIVE SOLUTION<br>TO TOURN YOUR VISITORS TO YOU CUSTOMER ?</p>
<div class="abs cta-button">
  <svg width="34" height="30" viewBox="0 0 34 30" aria-hidden="true"><path d="M2 15h28M20 5l10 10-10 10" stroke="#444" stroke-width="4" fill="none"/></svg>GET STARTED</div>

<section>
  <div class="abs voices-art" role="img" aria-label="Light grey illustration of a customer support agent with a speech bubble"></div>
  <h2 class="abs voices-title">SEE WHAT<br>OUR CUSTOMERS<br>ARE SAYING ABOUT<br>OUR SERVICE</h2>

  <div class="abs quote" style="top:898px">
    <div class="avatar" role="img" aria-label="Portrait photo of a female customer"></div>
    <p>We are Amazed with their service.&nbsp; this is just dummy text for now and real text will be here soon. This is just dummy text for now.</p>
    <cite>- Mara Ellison - Member of N.O.V.A</cite>
  </div>
  <div class="abs quote" style="top:989px">
    <div class="avatar" role="img" aria-label="Portrait photo of a male customer on the phone"></div>
    <p>We are Amazed with their service.&nbsp; this is just dummy text for now and real text will be here soon. This is just dummy text for now.</p>
    <cite>- Victor Haldane - Canopy corporation</cite>
  </div>
  <div class="abs quote" style="top:1081px">
    <div class="avatar" role="img" aria-label="Portrait photo of an older male customer"></div>
    <p>We are Amazed with their service.&nbsp; this is just dummy text for now and real text will be here soon. This is just dummy text for now.</p>
    <cite>- Owen Castell - Trivane</cite>
  </div>
</section>

<footer class="abs site-footer">Copyright 2014 - www.brightlaneads.com - All rights reserved.</footer>

</body>
</html>
```